Wine gifting platform needs redeem/decline page

Vintaro is a wine gifting platform. Users can send wine gifts to one or many people, the recipients will then receive an email with instructions on how to redeem their wine.

This is what we need: After clicking the link in the email they will be taken to the redeem/decline page/flow where they will choose their preferred wine and enter their shipping address. I have uploaded videos of both the decline and the redeem flows.

- All existing form fields, informational text, and error messages needs to be incorporated into the new design but otherwise you have creative freedom on presentation.
- We have four gift tiers: Silver, Gold, Platinum, and Diamond. We would like the redemption page to highlight this with different colors (or something else!) that's glanceable. I have attached screenshots to highlight these.
- Our target audience is professional and corporate but we want the redemption process to feel elegant and sleek. We want it to feel like a premium experience just like the wine they'll receive.

I would prefer Sketch files over Photoshop.

Target Market(s)

Professional, corporate

Number of Pages Required

3 page

Requirements
Must have
• All fields, all 3 steps of the wizard, information, and error messages/styles in the flow videos (attached)

```html
<!DOCTYPE html>
<html lang="en">
<head>
<meta charset="utf-8">
<title>Vintaro – Choose Your Gift</title>
<link href="https://fonts.googleapis.com/css2?family=Bree+Serif&family=Fira+Sans+Condensed:wght@400&family=Poppins:wght@400&display=swap" rel="stylesheet">
<style>
  :root {
    --brand: #0b44b0;
    --brand-dark: #0a3c9c;
    --page: #eff2fa;
    --panel: #94aedc;
    --line: #d3d9e6;
    --card-border: #b7c3dc;
    --ink: #121212;
    --white: #ffffff;
    --check-idle: #d6dfef;
  }
  * { box-sizing: border-box; margin: 0; padding: 0; }
  html, body { width: 1200px; height: 2464px; overflow: hidden; }
  body { background: var(--page); color: var(--ink); font-family: "Poppins", sans-serif; position: relative; }

  .site-header { height: 82px; background: var(--brand); display: flex; align-items: center; justify-content: center; }
  .brand-name { font-family: "Bree Serif", serif; font-size: 44px; color: var(--white); line-height: 1; }

  .wizard { position: absolute; top: 128px; left: 0; width: 1200px; height: 100px; }
  .wizard-step { position: absolute; width: 160px; text-align: center; }
  .wizard-step .num { width: 60px; height: 60px; margin: 0 auto; border-radius: 50%; background: var(--white); border: 4px solid #dde4f2;
    display: flex; align-items: center; justify-content: center; font-family: "Bree Serif", serif; font-size: 28px; color: var(--ink); }
  .wizard-step.active .num { color: var(--brand); }
  .wizard-step .label { margin-top: 12px; font-family: "Bree Serif", serif; font-size: 17px; color: var(--ink); }
  .wizard-step.active .label { color: var(--brand); }
  .wizard-arrow { position: absolute; top: 22px; }

  .divider { position: absolute; left: 60px; width: 1080px; height: 1px; background: var(--line); }

  .tier-tabs { position: absolute; top: 275px; left: 0; width: 1200px; display: flex; justify-content: center; gap: 7px; }
  .tier-tab { height: 35px; padding: 0 21px; border-radius: 8px; border: 1px solid var(--brand); background: var(--white);
    color: var(--brand); font-family: "Fira Sans Condensed", sans-serif; font-size: 15px; display: flex; align-items: center; }
  .tier-tab.active { background: var(--brand); color: var(--white); padding: 0 27px 0 22px; }

  .tier-intro { position: absolute; top: 349px; left: 60px; width: 1080px; height: 123px; background: var(--panel); border-radius: 10px; padding: 17px 25px 0 25px; }
  .tier-intro h2 { font-family: "Bree Serif", serif; font-weight: 400; font-size: 21px; color: var(--white); padding-bottom: 13px; border-bottom: 1px solid #aec1e4; }
  .tier-intro p { margin-top: 12px; font-size: 12.5px; line-height: 19px; color: var(--white); }

  .page-title { position: absolute; top: 495px; left: 61px; font-family: "Bree Serif", serif; font-weight: 400; font-size: 24px; }

  .category { position: absolute; left: 60px; width: 1080px; }
  .category-head { height: 36px; border-bottom: 1px solid var(--line); display: flex; align-items: flex-end; justify-content: space-between; padding: 0 2px 8px 2px; }
  .category-head h3 { font-family: "Bree Serif", serif; font-weight: 400; font-size: 24px; color: var(--brand); line-height: 1; }
  .pager { display: flex; gap: 6px; }
  .card-row { margin-top: 27px; display: flex; gap: 22px; margin-left: -1px; }
  .wine-card { position: relative; width: 254px; height: 316px; border: 1px solid var(--card-border); background: transparent; text-align: center; }
  .wine-card.selected { background: var(--white); border-color: var(--brand); }
  .select-check { position: absolute; top: 6px; right: 7px; }
  .bottle { width: 48px; height: 178px; margin: 21px auto 0; border-radius: 20px 20px 6px 6px; }
  .bottle.red { background: linear-gradient(180deg, #2a1a1d 0%, #3b1e24 45%, #c8c0b4 62%, #2a1a1d 80%); }
  .bottle.white { background: linear-gradient(180deg, #3c3a26 0%, #a69a5a 30%, #e7e1c2 60%, #8c8a70 100%); }
  .bottle.sparkling { background: linear-gradient(180deg, #1f6a36 0%, #1b1f1b 30%, #2a2e28 70%, #b48a3a 100%); }
  .bottle.rose { background: linear-gradient(180deg, #f3f0ee 0%, #f5c8b8 40%, #f0b39e 75%, #f4d6ca 100%); }
  .wine-name { margin-top: 20px; font-family: "Bree Serif", serif; font-size: 21px; line-height: 26px; color: var(--ink); }
  .detail-btn { display: inline-block; margin-top: 10px; width: 112px; height: 33px; line-height: 33px; border-radius: 6px; background: var(--brand);
    color: var(--white); font-family: "Fira Sans Condensed", sans-serif; font-size: 17px; }

  .next-btn { position: absolute; top: 2363px; left: 1043px; width: 97px; height: 33px; border-radius: 7px; background: var(--brand);
    color: var(--white); font-family: "Fira Sans Condensed", sans-serif; font-size: 16px; display: flex; align-items: center; justify-content: center; gap: 10px; }
</style>
</head>
<body>
  <header class="site-header"><span class="brand-name">Vintaro</span></header>

  <nav class="wizard" aria-label="Gift steps">
    <div class="wizard-step active" style="left:316px"><div class="num">1</div><div class="label">Choose Your Gift</div></div>
    <svg class="wizard-arrow" style="left:450px" width="104" height="16" viewBox="0 0 104 16"><line x1="1" y1="8" x2="92" y2="8" stroke="#0b44b0" stroke-width="1.2" stroke-dasharray="2 2"/><path d="M92 2 L103 8 L92 14 Z" fill="#0b44b0"/></svg>
    <div class="wizard-step" style="left:520px"><div class="num">2</div><div class="label">Enter Your Address</div></div>
    <svg class="wizard-arrow" style="left:648px" width="104" height="16" viewBox="0 0 104 16"><line x1="1" y1="8" x2="92" y2="8" stroke="#0b44b0" stroke-width="1.2" stroke-dasharray="2 2"/><path d="M92 2 L103 8 L92 14 Z" fill="#0b44b0"/></svg>
    <div class="wizard-step" style="left:720px"><div class="num">3</div><div class="label">Confirm</div></div>
  </nav>

  <div class="divider" style="top:250px"></div>

  <div class="tier-tabs">
    <span class="tier-tab active">Silver Collection</span>
    <span class="tier-tab">Gold Collection</span>
    <span class="tier-tab">Platinum Collection</span>
    <span class="tier-tab">Diamond Collection</span>
  </div>

  <section class="tier-intro">
    <h2>Silver Collection</h2>
    <p>At Vintaro we hand select every last bottle we send. We work with some of the world's best sommeliers to make sure you always get a great bottle.<br>simply choose your preferred type of wind and let us do the hard work for you.</p>
  </section>

  <h1 class="page-title">Choose your gift from the silver Collection</h1>

  <section class="category" style="top:574px">
    <div class="category-head"><h3>Red</h3>
      <div class="pager">
        <svg width="10" height="16" viewBox="0 0 10 16"><path d="M8 2 L2 8 L8 14" fill="none" stroke="#0b44b0" stroke-width="2"/></svg>
        <svg width="10" height="16" viewBox="0 0 10 16"><path d="M2 2 L8 8 L2 14" fill="none" stroke="#121212" stroke-width="2"/></svg>
      </div>
    </div>
    <div class="card-row">
      <article class="wine-card selected">
        <svg class="select-check" width="40" height="40" viewBox="0 0 40 40"><circle cx="20" cy="20" r="19" fill="#0b44b0"/><path d="M11 20 L17.5 27 L29 13" fill="none" stroke="#fff" stroke-width="3"/></svg>
        <div class="bottle red" role="img" aria-label="Pinot Noir bottle"></div>
        <div class="wine-name">Pianot Noir</div><span class="detail-btn">View Detail</span>
      </article>
      <article class="wine-card">
        <svg class="select-check" width="40" height="40" viewBox="0 0 40 40"><circle cx="20" cy="20" r="19" fill="#d6dfef"/><path d="M11 20 L17.5 27 L29 13" fill="none" stroke="#fff" stroke-width="3"/></svg>
        <div class="bottle red" role="img" aria-label="Zinfandel bottle"></div>
        <div class="wine-name">Zinfandel</div><span class="detail-btn">View Detail</span>
      </article>
      <article class="wine-card">
        <svg class="select-check" width="40" height="40" viewBox="0 0 40 40"><circle cx="20" cy="20" r="19" fill="#d6dfef"/><path d="M11 20 L17.5 27 L29 13" fill="none" stroke="#fff" stroke-width="3"/></svg>
        <div class="bottle red" role="img" aria-label="Sangiovese bottle"></div>
        <div class="wine-name">Sangiovese</div><span class="detail-btn">View Detail</span>
      </article>
      <article class="wine-card">
        <svg class="select-check" width="40" height="40" viewBox="0 0 40 40"><circle cx="20" cy="20" r="19" fill="#d6dfef"/><path d="M11 20 L17.5 27 L29 13" fill="none" stroke="#fff" stroke-width="3"/></svg>
        <div class="bottle red" role="img" aria-label="Cabernet Sauvignon bottle"></div>
        <div class="wine-name">Cabernet Sauvignon</div><span class="detail-btn">View Detail</span>
      </article>
    </div>
  </section>

  <section class="category" style="top:1039px">
    <div class="category-head"><h3>White</h3></div>
    <div class="card-row">
      <article class="wine-card">
        <svg class="select-check" width="40" height="40" viewBox="0 0 40 40"><circle cx="20" cy="20" r="19" fill="#d6dfef"/><path d="M11 20 L17.5 27 L29 13" fill="none" stroke="#fff" stroke-width="3"/></svg>
        <div class="bottle white" role="img" aria-label="Chardonnay bottle"></div>
        <div class="wine-name">Chardonny</div><span class="detail-btn">View Detail</span>
      </article>
      <article class="wine-card">
        <svg class="select-check" width="40" height="40" viewBox="0 0 40 40"><circle cx="20" cy="20" r="19" fill="#d6dfef"/><path d="M11 20 L17.5 27 L29 13" fill="none" stroke="#fff" stroke-width="3"/></svg>
        <div class="bottle white" role="img" aria-label="Pinot Grigio bottle"></div>
        <div class="wine-name">Pinot Grigio</div><span class="detail-btn">View Detail</span>
      </article>
      <article class="wine-card">
        <svg class="select-check" width="40" height="40" viewBox="0 0 40 40"><circle cx="20" cy="20" r="19" fill="#d6dfef"/><path d="M11 20 L17.5 27 L29 13" fill="none" stroke="#fff" stroke-width="3"/></svg>
        <div class="bottle white" role="img" aria-label="Sauvignon Blanc bottle"></div>
        <div class="wine-name">Sauvignon Blanc</div><span class="detail-btn">View Detail</span>
      </article>
      <article class="wine-card">
        <svg class="select-check" width="40" height="40" viewBox="0 0 40 40"><circle cx="20" cy="20" r="19" fill="#d6dfef"/><path d="M11 20 L17.5 27 L29 13" fill="none" stroke="#fff" stroke-width="3"/></svg>
        <div class="bottle white" role="img" aria-label="Riesling bottle"></div>
        <div class="wine-name">Riesling</div><span class="detail-btn">View Detail</span>
      </article>
    </div>
  </section>

  <section class="category" style="top:1496px">
    <div class="category-head"><h3>Sparkling</h3></div>
    <div class="card-row">
      <article class="wine-card">
        <svg class="select-check" width="40" height="40" viewBox="0 0 40 40"><circle cx="20" cy="20" r="19" fill="#d6dfef"/><path d="M11 20 L17.5 27 L29 13" fill="none" stroke="#fff" stroke-width="3"/></svg>
        <div class="bottle sparkling" role="img" aria-label="Prosecco bottle"></div>
        <div class="wine-name">Prosecco</div><span class="detail-btn">View Detail</span>
      </article>
      <article class="wine-card">
        <svg class="select-check" width="40" height="40" viewBox="0 0 40 40"><circle cx="20" cy="20" r="19" fill="#d6dfef"/><path d="M11 20 L17.5 27 L29 13" fill="none" stroke="#fff" stroke-width="3"/></svg>
        <div class="bottle sparkling" role="img" aria-label="Cava bottle"></div>
        <div class="wine-name">Cava</div><span class="detail-btn">View Detail</span>
      </article>
    </div>
  </section>

  <section class="category" style="top:1938px">
    <div class="category-head"><h3>Rose</h3></div>
    <div class="card-row">
      <article class="wine-card">
        <svg class="select-check" width="40" height="40" viewBox="0 0 40 40"><circle cx="20" cy="20" r="19" fill="#d6dfef"/><path d="M11 20 L17.5 27 L29 13" fill="none" stroke="#fff" stroke-width="3"/></svg>
        <div class="bottle rose" role="img" aria-label="Rosé bottle"></div>
        <div class="wine-name">Rose</div><span class="detail-btn">View Detail</span>
      </article>
    </div>
  </section>

  <div class="divider" style="top:2347px"></div>

  <span class="next-btn">Next
    <svg width="26" height="12" viewBox="0 0 26 12"><line x1="1" y1="6" x2="24" y2="6" stroke="#fff" stroke-width="1.6"/><path d="M18 1 L24.5 6 L18 11" fill="none" stroke="#fff" stroke-width="1.6"/></svg>
  </span>
</body>
</html>
```